Poster Design Project

Simple, very easy design project.

Design for a 20" x 30" poster (I will print the poster, you do the high-res design), of the attached.

(Pls note, this JPG is sideways and is an error). You are designing PORTRAIT

```html
<!DOCTYPE html>
<html lang="en">
<head>
<meta charset="utf-8">
<title>Great Ecommerce Poster</title>
<link href="https://fonts.googleapis.com/css2?family=Krona+One&family=Stint+Ultra+Condensed&display=swap" rel="stylesheet">
<style>
  :root {
    --paper: #ffffff;
    --blue-deep: #1f4fae;
    --blue-mid: #3a76d2;
    --blue-glow: #bfe4ff;
    --panel: rgba(190, 196, 238, 0.78);
    --ink: #000000;
    --title: #ffffff;
  }
  html, body {
    margin: 0;
    padding: 0;
    width: 825px;
    height: 1200px;
    overflow: hidden;
    background: var(--paper);
  }
  .poster {
    position: relative;
    width: 825px;
    height: 1200px;
    background: var(--paper);
  }
  .poster__backdrop {
    position: absolute;
    left: 35px;
    top: 31px;
    width: 757px;
    height: 1136px;
    background:
      radial-gradient(circle at 12% 4%, rgba(255,255,255,0.9) 0, rgba(191,228,255,0.55) 60px, transparent 230px),
      radial-gradient(circle at 88% 96%, rgba(255,255,255,0.85) 0, rgba(191,228,255,0.5) 50px, transparent 220px),
      radial-gradient(circle at 8% 88%, rgba(191,228,255,0.55) 0, transparent 180px),
      radial-gradient(circle at 92% 30%, rgba(191,228,255,0.45) 0, transparent 200px),
      linear-gradient(160deg, var(--blue-mid) 0%, var(--blue-deep) 55%, var(--blue-mid) 100%);
  }
  .poster__title {
    position: absolute;
    left: 35px;
    width: 757px;
    top: 138px;
    margin: 0;
    text-align: center;
    font-family: "Krona One", sans-serif;
    font-weight: 400;
    color: var(--title);
    line-height: 84px;
    text-shadow: 4px 4px 0 var(--ink);
  }
  .poster__title-line {
    display: block;
  }
  .poster__title-line--first { font-size: 66px; }
  .poster__title-line--second { font-size: 70px; letter-spacing: -1px; }
  .values-panel {
    position: absolute;
    left: 144px;
    top: 322px;
    width: 545px;
    height: 709px;
    border-radius: 72px;
    background: var(--panel);
  }
  .values-list {
    list-style: none;
    margin: 0;
    padding: 0;
    position: absolute;
    left: 35px;
    width: 757px;
    top: 366px;
    text-align: center;
    font-family: "Stint Ultra Condensed", serif;
    font-size: 84px;
    line-height: 98.5px;
    color: var(--ink);
    -webkit-text-stroke: 1.2px var(--ink);
  }
</style>
</head>
<body>
  <main class="poster">
    <div class="poster__backdrop" role="img" aria-label="Glowing blue digital circuit-board background with light flares"></div>
    <h1 class="poster__title">
      <span class="poster__title-line poster__title-line--first">GREAT</span>
      <span class="poster__title-line poster__title-line--second">ECOMMERCE</span>
    </h1>
    <div class="values-panel"></div>
    <ul class="values-list">
      <li>Diversity Of Thought</li>
      <li>Desire To Learn</li>
      <li>Never Settle</li>
      <li>Be A Problem Solver</li>
      <li>Work Fast (Web Speed)</li>
      <li>Execution - A Way Of Life</li>
    </ul>
  </main>
</body>
</html>
```